I need the following
2 versions (CMYK and RGB)
Full Page ad design 7.5" wide x 10" tall
No less than 300 dpi for print and 72dpi for web:
Full Color CMYK for print and RGB for web
Provide a high quality JPEG of the ad as well.

You can use the attached post card as a guide and use the info within it. You can get more information from our website at HaulingCrewFolks.net.
Also add a block with the following ... We work with real estate agents to make moving stress - free for their clients:
*Old Fashioned Customer Service
*Discounted rates
*Always Free Estimates
*Fully Licensed and Insured
*Communication From Start To Finish
*Full Service Moving

```html
<!DOCTYPE html>
<html lang="en">
<head>
<meta charset="utf-8">
<title>HaulingCrewFolks – Full Page Ad</title>
<link href="https://fonts.googleapis.com/css2?family=Poppins:wght@400;500;600;700;800&family=Yellowtail&display=swap" rel="stylesheet">
<style>
:root{
  --orange:#e9a04a;
  --orange-deep:#e39437;
  --dark:#262626;
  --dark-2:#1c1c1c;
  --pill:#4a4a4a;
  --light:#efefef;
  --white:#ffffff;
  --ink:#1f1f1f;
  --line:#bdbdbd;
  --page:#e9e9e9;
}
*{margin:0;padding:0;box-sizing:border-box}
html,body{width:783px;height:1200px;overflow:hidden;background:var(--page)}
body{font-family:"Poppins",sans-serif;color:var(--ink)}
.ad{position:absolute;left:0;top:78px;width:783px;height:1044px;overflow:hidden;background:var(--white)}

/* header */
.hero{position:absolute;left:0;top:0;width:783px;height:458px;background:linear-gradient(135deg,#333 0%,#262626 55%,#1f1f1f 100%)}
.hero-photo{position:absolute;left:455px;top:28px;width:328px;height:382px;background:radial-gradient(ellipse at 55% 60%,#e8792a 0%,#c9a77a 45%,#3a3a3a 80%);opacity:.9}
.brand{position:absolute;left:44px;top:58px;font-weight:600;font-size:24px;color:var(--orange);letter-spacing:.2px}
.headline{position:absolute;left:40px;top:108px;font-weight:800;font-size:74px;line-height:1;color:var(--orange);letter-spacing:-1px}
.tagline{position:absolute;left:46px;top:189px;width:362px;height:46px;border-radius:4px 24px 24px 4px;background:var(--pill)}
.tagline span{position:absolute;left:14px;top:0;font-family:"Yellowtail",cursive;font-size:38px;line-height:46px;color:var(--white)}
.stress{position:absolute;left:44px;top:238px;font-weight:800;font-size:52px;line-height:1;color:var(--white)}
.rule{position:absolute;left:46px;top:300px;width:364px;height:1px;background:#6a6a6a}
.quote-mark{position:absolute;left:46px;top:312px;font-weight:800;font-size:30px;line-height:1;color:var(--orange)}
.testimonial{position:absolute;left:74px;top:328px;width:354px;font-size:10.2px;line-height:12.3px;color:var(--white)}
.reviewer{position:absolute;left:248px;top:408px;width:180px;text-align:right;font-size:10px;font-weight:700;color:var(--orange)}
.reviewer b{letter-spacing:1px;margin-right:2px}
.hero-stripes{position:absolute;left:0;top:410px}

/* agents block */
.agents{position:absolute;left:0;top:458px;width:783px;height:194px;background:var(--light)}
.agents h2{position:absolute;left:48px;top:22px;font-weight:700;font-size:19.5px;line-height:25px;color:var(--ink)}
.agents h2 em{font-style:normal;color:var(--orange-deep);display:block}
.agents .divider{position:absolute;left:48px;top:80px;width:675px;height:1px;background:var(--line)}
.perk{position:absolute;display:flex;gap:8px;font-weight:600;font-size:14.5px;line-height:17px;color:var(--ink)}
.perk svg{flex:0 0 13px;margin-top:2px}

/* rates */
.rates-title{position:absolute;left:0;width:783px;top:664px;text-align:center;font-weight:700;font-size:26px;line-height:34px;color:var(--ink)}
.rates-title em{font-style:normal;color:var(--orange-deep)}
.rates-frame{position:absolute;left:0;top:0}
.card{position:absolute;top:724px;width:170px;height:158px;border-radius:12px;overflow:hidden;background:var(--dark-2)}
.card::after{content:"";position:absolute;left:0;right:0;bottom:0;height:76px;background:var(--orange)}
.card-inner{position:absolute;inset:8px;border:1.5px dashed rgba(255,255,255,.85);border-radius:8px;z-index:1;text-align:center;color:var(--white)}
.card .off{margin-top:10px;font-weight:700;font-size:31px;line-height:34px}
.card .off sup{font-size:15px;vertical-align:13px;margin-right:1px}
.card .moves{font-weight:700;font-size:17px;line-height:20px}
.card .amount{margin-top:16px;font-weight:800;font-size:28px;line-height:30px}
.card .fine{font-size:8px;line-height:12px;color:#fff6ea}
.license{position:absolute;left:233px;top:898px;width:318px;height:34px;border-radius:12px 12px 0 0;background:var(--orange);text-align:center;font-size:18px;line-height:34px;color:var(--white)}
.license b{font-weight:700}
.boxes{position:absolute;background:linear-gradient(160deg,#d7a76a 0%,#c08a4c 60%,#a3713b 100%)}
.boxes-left{left:0;top:784px;width:145px;height:152px;clip-path:polygon(0 18%,45% 0,70% 10%,100% 40%,100% 100%,0 100%)}
.boxes-right{left:606px;top:828px;width:177px;height:216px;clip-path:polygon(40% 18%,70% 0,100% 4%,100% 100%,0 100%,0 80%,30% 60%)}

/* footer */
.footer{position:absolute;left:0;top:949px;width:783px;height:95px}
.call{position:absolute;left:44px;top:958px;color:var(--white)}
.call p{font-size:18.5px;line-height:22px}
.call strong{display:block;font-weight:700;font-size:26px;line-height:32px;color:var(--dark-2)}
.contact{position:absolute;left:348px;top:968px;color:var(--white);font-weight:600;font-size:15px;line-height:26px}
.contact li{list-style:none;display:flex;align-items:center;gap:8px}
</style>
</head>
<body>
<main class="ad">

  <section class="hero">
    <div class="hero-photo" role="img" aria-label="Photo of a smiling mover in an orange uniform carrying a cardboard box"></div>
    <div class="brand">HaulingCrewFolks</div>
    <h1 class="headline">MOVING?</h1>
    <div class="tagline"><span>We'll make your move</span></div>
    <div class="stress">STRESS-FREE!</div>
    <div class="rule"></div>
    <div class="quote-mark">&ldquo;</div>
    <p class="testimonial">Best movers in Dallas! They were fast, efficient, on time and very reasonably priced. They took so much care with our belongings. We have moved about 15 times and they are the best movers we have ever had. Highly recommend to anyone looking for movers. We really appreciate the care that they handled our furniture with. We will definitely be using them again. Thank you Tom and team!</p>
    <div class="reviewer"><b>★★★★★</b>-DANA WHITFIELD</div>
    <svg class="hero-stripes" width="783" height="48" viewBox="0 0 783 48" aria-hidden="true">
      <polygon points="482,42 506,8 526,8 502,42" fill="var(--dark-2)"/>
      <polygon points="508,42 532,8 552,8 528,42" fill="var(--dark-2)"/>
      <polygon points="534,42 558,8 578,8 554,42" fill="var(--orange)"/>
      <polygon points="552,48 586,8 783,8 783,48" fill="var(--orange)"/>
    </svg>
  </section>

  <section class="agents">
    <h2>WE WORK WITH REAL ESTATE AGENTS TO MAKE MOVING <em>STRESS FREE FOR THEIR CLIENTS</em></h2>
    <div class="divider"></div>
    <div class="perk" style="left:48px;top:104px"><svg width="13" height="13" viewBox="0 0 13 13"><circle cx="6.5" cy="6.5" r="6.5" fill="var(--orange)"/><path d="M3.6 6.7l2 2 3.8-4" stroke="#fff" stroke-width="1.5" fill="none"/></svg><span>Old Fashioned<br>Customer Service</span></div>
    <div class="perk" style="left:48px;top:158px"><svg width="13" height="13" viewBox="0 0 13 13"><circle cx="6.5" cy="6.5" r="6.5" fill="var(--orange)"/><path d="M3.6 6.7l2 2 3.8-4" stroke="#fff" stroke-width="1.5" fill="none"/></svg><span>Discounted rates</span></div>
    <div class="perk" style="left:268px;top:104px"><svg width="13" height="13" viewBox="0 0 13 13"><circle cx="6.5" cy="6.5" r="6.5" fill="var(--orange)"/><path d="M3.6 6.7l2 2 3.8-4" stroke="#fff" stroke-width="1.5" fill="none"/></svg><span>Always Free Estimates</span></div>
    <div class="perk" style="left:268px;top:140px"><svg width="13" height="13" viewBox="0 0 13 13"><circle cx="6.5" cy="6.5" r="6.5" fill="var(--orange)"/><path d="M3.6 6.7l2 2 3.8-4" stroke="#fff" stroke-width="1.5" fill="none"/></svg><span>Fully Licensed and<br>Insured</span></div>
    <div class="perk" style="left:515px;top:104px"><svg width="13" height="13" viewBox="0 0 13 13"><circle cx="6.5" cy="6.5" r="6.5" fill="var(--orange)"/><path d="M3.6 6.7l2 2 3.8-4" stroke="#fff" stroke-width="1.5" fill="none"/></svg><span>Communication From<br>To Finish</span></div>
    <div class="perk" style="left:515px;top:158px"><svg width="13" height="13" viewBox="0 0 13 13"><circle cx="6.5" cy="6.5" r="6.5" fill="var(--orange)"/><path d="M3.6 6.7l2 2 3.8-4" stroke="#fff" stroke-width="1.5" fill="none"/></svg><span>Full Service Moving</span></div>
  </section>

  <section class="rates">
    <svg class="rates-frame" width="783" height="900" viewBox="0 0 783 900" aria-hidden="true">
      <polyline points="248,681 52,681 52,856" fill="none" stroke="var(--line)" stroke-width="1.2"/>
      <polyline points="535,681 734,681 734,856" fill="none" stroke="var(--line)" stroke-width="1.2"/>
      <line x1="248" y1="699" x2="535" y2="699" stroke="var(--line)" stroke-width="1"/>
      <rect x="372" y="697" width="38" height="4" rx="2" fill="var(--orange)"/>
      <circle cx="272" cy="681" r="2" fill="var(--orange)"/>
      <circle cx="511" cy="681" r="2" fill="var(--orange)"/>
    </svg>
    <h2 class="rates-title">SPECIAL <em>RATES</em></h2>

    <div class="boxes boxes-left" role="img" aria-label="Stack of cardboard moving boxes"></div>
    <div class="boxes boxes-right" role="img" aria-label="Stack of cardboard moving boxes"></div>

    <div class="card" style="left:102px"><div class="card-inner">
      <div class="off"><sup>$</sup>25 OFF</div><div class="moves">MOVES UNDER</div>
      <div class="amount">$500</div><div class="fine">With this card. Call for details.</div>
    </div></div>
    <div class="card" style="left:305px"><div class="card-inner">
      <div class="off"><sup>$</sup>50 OFF</div><div class="moves">MOVES OVER</div>
      <div class="amount">$500</div><div class="fine">With this card. Call for details.</div>
    </div></div>
    <div class="card" style="left:506px"><div class="card-inner">
      <div class="off"><sup>$</sup>100 OFF</div><div class="moves">MOVES OVER</div>
      <div class="amount">$500</div><div class="fine">With this card. Call for details.</div>
    </div></div>

    <div class="license"><b>TXDMV:</b> 001234567C</div>
  </section>

  <footer>
    <svg class="footer" width="783" height="95" viewBox="0 0 783 95" aria-hidden="true">
      <rect x="0" y="0" width="783" height="95" fill="var(--dark-2)"/>
      <polygon points="0,0 312,0 352,95 0,95" fill="var(--orange)"/>
    </svg>
    <div class="call"><p>Call us today to get started!</p><strong>(972) 555-0148</strong></div>
    <ul class="contact">
      <li><svg width="14" height="11" viewBox="0 0 14 11"><rect x=".6" y=".6" width="12.8" height="9.8" fill="none" stroke="var(--orange)" stroke-width="1.2"/><path d="M.6 .6l6.4 5 6.4-5" fill="none" stroke="var(--orange)" stroke-width="1.2"/></svg>hello@haulingcrewfolks.net</li>
      <li><svg width="14" height="14" viewBox="0 0 14 14"><g fill="none" stroke="var(--orange)" stroke-width="1.1"><circle cx="7" cy="7" r="6.2"/><ellipse cx="7" cy="7" rx="2.8" ry="6.2"/><line x1=".8" y1="7" x2="13.2" y2="7"/><line x1="2" y1="3.6" x2="12" y2="3.6"/><line x1="2" y1="10.4" x2="12" y2="10.4"/></g></svg>haulingcrewfolks.net</li>
    </ul>
  </footer>

</main>
</body>
</html>
```